Brookmere Recovery Center Billboard (Addiction / Alcohol / Opioid )

visit www.brookmererecovery-example.com
We are an inpatient treatment center for opioid, alcohol and drug addiction. We are looking to get multiple 12'x25' billboards in our area. Our Phone number is 1-855-CALM-NOW we are located in Auburn Indiana
We pride ourselves on a comfortable medical detox and treat our patients as family.

Target Market(s)

Current Addicts, Addicts family or friends, Factory Workers and Shopvane shoppers

Industry/Entity Type

Health Care

Font styles to use
Sans Serif

Colors
0355a3
3176b5
ffffff

Requirements
Must have
• Logo and Phone number, and Brookmere Recovery
Nice to have
• Ideas?
1.) Addiction hurts more than yourself. (Pic of little girl?)
2.) Just how much are you willing to lose?
3.) Addiction does not define you, You are what you choose to become.
4.) Indiana's most comfortable Detox
5.) Detox in unmatched comfort.
6.) Background could be patient room with logo in upper right
7.) Looking to be able to read easily from road.
Should not have
• Hard to read lettering

```html
<!DOCTYPE html>
<html lang="en">
<head>
<meta charset="utf-8">
<title>Brookmere Recovery Billboard</title>
<link rel="stylesheet" href="https://fonts.googleapis.com/css2?family=Archivo:wght@700;800;900&family=Montserrat:wght@500&display=swap">
<style>
  :root {
    --navy: #0e2a68;
    --cyan: #00c6f0;
    --white: #ffffff;
    --ink: #1a1a1a;
    --page: #ffffff;
    --photo-light: #d9d9d9;
    --photo-mid: #a9aaac;
    --photo-warm: #c9825a;
  }
  * { margin: 0; padding: 0; box-sizing: border-box; }
  html, body {
    width: 971px; height: 1200px; overflow: hidden;
    background: var(--page);
  }
  .billboard {
    position: absolute; left: 36px; top: 384px;
    width: 900px; height: 431px;
    background: var(--white);
    box-shadow: 0 2px 6px rgba(0,0,0,.25);
    overflow: hidden;
    font-family: "Archivo", Arial, sans-serif;
  }
  .brand {
    position: absolute; left: 0; width: 540px; top: 18px;
    display: flex; flex-direction: column; align-items: center; gap: 8px;
  }
  .brand-mark {
    width: 46px; height: 46px; border-radius: 50%;
    background: var(--cyan);
  }
  .brand-name {
    font-family: "Montserrat", Arial, sans-serif; font-weight: 500;
    font-size: 15px; letter-spacing: .5px; color: var(--navy);
    text-transform: uppercase;
  }
  .headline {
    position: absolute; left: 0; width: 540px; top: 115px;
    text-align: center; font-weight: 900; font-size: 40px;
    line-height: 43px; color: var(--navy); letter-spacing: .3px;
  }
  .headline .accent { color: var(--cyan); }
  .services {
    position: absolute; left: 0; top: 219px; width: 556px; height: 55px;
    background: var(--cyan);
    clip-path: polygon(0 0, 543px 0, 556px 55px, 0 55px);
    display: flex;
  }
  .service {
    display: flex; align-items: center; gap: 8px;
    padding-left: 19px; height: 100%;
    color: var(--white); font-weight: 800; font-size: 21px;
    border-right: 2px solid var(--white);
  }
  .service:nth-child(1) { width: 194px; }
  .service:nth-child(2) { width: 201px; padding-left: 10px; }
  .service:nth-child(3) { border-right: none; padding-left: 8px; }
  .service-icon {
    width: 36px; height: 36px; border-radius: 50%;
    background: var(--white); border: 2px solid var(--navy);
    display: flex; align-items: center; justify-content: center;
    flex: none;
  }
  .visit {
    position: absolute; left: 0; width: 540px; top: 289px;
    text-align: center; font-weight: 800; font-size: 21px; color: var(--ink);
    letter-spacing: .5px;
  }
  .url {
    position: absolute; left: 0; width: 540px; top: 323px;
    text-align: center; font-weight: 800; font-size: 24px; color: var(--navy);
  }
  .contact-band {
    position: absolute; left: 0; right: 0; bottom: 0; height: 67px;
    background: var(--navy); color: var(--white);
    display: flex; align-items: center; justify-content: center;
    font-weight: 800; font-size: 42px; letter-spacing: .5px;
  }
  .accent-stripe {
    position: absolute; left: 0; top: 0; width: 900px; height: 364px;
  }
  .photo {
    position: absolute; left: 0; top: 0; width: 900px; height: 356px;
    background:
      radial-gradient(ellipse 70px 140px at 730px 230px, var(--photo-warm) 0%, rgba(201,130,90,0) 100%),
      linear-gradient(180deg, var(--photo-light) 0%, #c4c5c7 55%, var(--photo-mid) 100%);
    clip-path: polygon(540px 0, 900px 0, 900px 356px, 616px 356px);
  }
</style>
</head>
<body>
  <main class="billboard">
    <div class="photo" role="img" aria-label="Photo of a young girl with long red hair standing thoughtfully in a comfortable patient room with wall-mounted TVs"></div>

    <svg class="accent-stripe" viewBox="0 0 900 364" aria-hidden="true">
      <polygon points="500,0 532,0 613,356 579,356" fill="var(--navy)"/>
    </svg>

    <header class="brand">
      <span class="brand-mark"></span>
      <span class="brand-name">Brookmere Recovery</span>
    </header>

    <h1 class="headline">
      ADDICTION <span class="accent">HURTS</span><br>
      MORE THAN <span class="accent">YOURSELF</span>
    </h1>

    <ul class="services">
      <li class="service">
        <span class="service-icon">
          <svg width="18" height="22" viewBox="0 0 18 22" aria-hidden="true">
            <rect x="6" y="1" width="6" height="4" fill="var(--navy)"/>
            <rect x="3" y="6" width="12" height="15" rx="2" fill="var(--navy)"/>
            <rect x="6" y="10" width="6" height="7" fill="var(--white)"/>
          </svg>
        </span>
        ALCOHOL
      </li>
      <li class="service">
        <span class="service-icon">
          <svg width="22" height="22" viewBox="0 0 22 22" aria-hidden="true">
            <circle cx="14" cy="8" r="6" fill="var(--navy)"/>
            <circle cx="8" cy="14" r="6" fill="var(--navy)" stroke="var(--white)" stroke-width="1.5"/>
          </svg>
        </span>
        ADDICTION
      </li>
      <li class="service">
        <span class="service-icon">
          <svg width="24" height="16" viewBox="0 0 24 16" aria-hidden="true">
            <path d="M1 8 Q12 -4 23 8 Q12 20 1 8 Z" fill="none" stroke="var(--navy)" stroke-width="2"/>
            <circle cx="12" cy="8" r="4" fill="none" stroke="var(--navy)" stroke-width="2"/>
            <circle cx="12" cy="8" r="1.5" fill="var(--navy)"/>
          </svg>
        </span>
        OPIOID
      </li>
    </ul>

    <p class="visit">VISIT OUR WEBSITE</p>
    <p class="url">www.brookmererecovery-example.com</p>

    <footer class="contact-band">Contact us - 1-855-CALM-NOW</footer>
  </main>
</body>
</html>
```